Valdorick Business Card Design

Valdorick is the holdings company for my portfolio of businesses. These businesses currently only include Valdorick Advising. V|A is a strategic consulting firm that focuses on small businesses and start-ups that want help with their brand. We focus on partnering with influencers (Pro Athletes and Celebrities) and Social Media Marketing. We also want to focus on companies that have a positive effect on the community or world. The audience I am going after is very corporate. I want to have the corporate edge with some 25yr old flair.
Industry/Entity Type
Business
Contact Information for Business Card
General Idea AttachedLogo (Attached)Jonathan R. MasonCEO & Managing MemberDown Left Bottom CornerPhone: 347-570-0585Cell: 240-604-7930mason@valdorick-example.comDown Right Bottom Corner 174 W 4th St, Ste 212New York, NY 10014www.valdorick-example.comBackside LogoI want the entire card extra thick and with metallic finish
Look and feel

```html
<!DOCTYPE html>
<html lang="en">
<head>
<meta charset="utf-8">
<title>Valdorick Holdings – Business Card</title>
<link rel="stylesheet" href="https://fonts.googleapis.com/css2?family=Tinos:wght@400&display=swap">
<style>
  :root {
    --stage: #2e2e30;
    --card-black: #141414;
    --card-white: #ffffff;
    --ink: #111111;
    --brand-red: #8e1414;
    --silver: #b9b9bd;
    --edge: #0b0b0b;
  }
  * { margin: 0; padding: 0; box-sizing: border-box; }
  html, body { width: 1200px; height: 1000px; overflow: hidden; }
  body {
    background: var(--stage);
    font-family: "Tinos", "Times New Roman", serif;
    color: var(--ink);
    display: flex;
    flex-direction: column;
    align-items: center;
    justify-content: center;
    gap: 60px;
  }
  .card {
    width: 700px;
    height: 400px;
    position: relative;
    box-shadow: 0 14px 34px rgba(0,0,0,.45);
  }
  /* Back side */
  .card-back {
    background: var(--card-black);
    display: flex;
    align-items: center;
    justify-content: center;
  }
  .brand {
    display: flex;
    align-items: center;
    gap: 18px;
  }
  .brand-square {
    width: 64px;
    height: 64px;
    background: var(--brand-red);
  }
  .brand-name {
    font-size: 44px;
    letter-spacing: 1px;
    line-height: 1;
  }
  .card-back .brand-name { color: var(--silver); }
  .card-back .brand-square { background: var(--silver); }

  /* Front side */
  .card-front {
    background: var(--card-white);
    border-bottom: 18px solid var(--edge);
  }
  .card-front .brand {
    position: absolute;
    left: 50px;
    top: 50px;
    gap: 16px;
  }
  .card-front .brand-square { width: 58px; height: 58px; }
  .card-front .brand-name { color: var(--brand-red); font-size: 40px; }
  .holder {
    position: absolute;
    left: 230px;
    top: 170px;
    width: 400px;
    text-align: center;
  }
  .holder-name { font-size: 34px; letter-spacing: .5px; }
  .holder-title { font-size: 19px; margin-top: 4px; }
  .contact {
    position: absolute;
    bottom: 36px;
    font-size: 14px;
    line-height: 1.45;
  }
  .contact-direct { left: 40px; }
  .contact-office { right: 40px; text-align: left; }
</style>
</head>
<body>
  <section class="card card-back" aria-label="Card back">
    <div class="brand">
      <span class="brand-square"></span>
      <span class="brand-name">Valdorick Holdings LLC</span>
    </div>
  </section>

  <section class="card card-front" aria-label="Card front">
    <div class="brand">
      <span class="brand-square"></span>
      <span class="brand-name">Valdorick Holdings LLC</span>
    </div>
    <div class="holder">
      <div class="holder-name">Derrick L. Fanshaw</div>
      <div class="holder-title">CEO &amp; Managing Member</div>
    </div>
    <address class="contact contact-direct" style="font-style:normal">
      Phone: 347-555-0162<br>
      Cell: 240-555-0187<br>
      fanshaw@valdorick-example.com
    </address>
    <address class="contact contact-office" style="font-style:normal">
      88 E 9th St, Ste 405<br>
      New York, NY 10099<br>
      www.valdorick-example.com
    </address>
  </section>
</body>
</html>
```